Tailmart.com Dog Coupon Site Website Design

FurSaver - Dog Coupon Site Design Brief

Project Overview
**Site Name:** TailMart.com
**Purpose:** A modern coupon aggregation platform specifically for dog and pet-related products and services
**Target Audience:** Dog owners, pet enthusiasts, budget-conscious pet parents

Brand Identity & Visual Direction

Typography
- **Headers:** Modern sans-serif (Inter or similar) - Clean and friendly
- **Body:** Readable sans-serif with good mobile legibility
- **Accent:** Playful but professional font for coupon codes

Design Principles
- **Flat Design:** Clean, minimal with subtle shadows
- **Friendly & Approachable:** Rounded corners, soft edges
- **Trust-Building:** Clear pricing, transparent savings
- **Scannable:** Easy-to-read coupon codes and offers

## User Experience & Functionality

### Homepage Features
1. **Hero Section**
- Clear value proposition
- Search functionality
- Featured savings highlight

2. **Coupon Cards**
- One-click copy functionality
- Clear discount display
- Store/brand logos
- Expiration dates
- "Get Deal" call-to-action

3. **Navigation**
- Categories (Food, Toys, Health, Services, etc.)
- Popular stores
- Latest deals

### Interactive Elements
- **Copy Button:** Instant feedback when coupon copied
- **Deal Pages:** Detailed offer information, terms, store details
- **Search & Filter:** By category, store, discount amount
- **Mobile Menu:** Hamburger navigation for mobile

## Technical Requirements

### Responsive Design
- **Mobile-First:** Optimized for touch interactions
- **Tablet:** Adapted layout for medium screens
- **Desktop:** Full-width utilization with sidebar potential

### Performance
- **Fast Loading:** Optimized images, minimal JavaScript
- **Accessibility:** WCAG compliant, screen reader friendly
- **SEO Optimized:** Structured data for deals and offers

## Content Strategy

### Deal Categories
- Dog Food & Treats
- Toys & Accessories
- Health & Grooming
- Training & Services
- Outdoor & Travel

### Key Messaging
- "Save on everything your dog loves"
- "Verified deals updated daily"
- "Your pup deserves the best for less"

## Conversion Optimization

### Trust Elements
- Deal verification badges
- User reviews/ratings
- Clear savings calculations
- Expiration date transparency

### Call-to-Actions
- "Copy Code" (primary action)
- "Get Deal" (secondary action)
- "View All [Store] Deals"

## Success Metrics
- Coupon copy rate
- Click-through to retailer
- User return visits
- Mobile vs desktop usage
- Category performance

This design brief ensures a user-friendly, trustworthy platform that makes finding and using pet deals effortless while maintaining a warm, dog-loving community feel.

1. Design Objective
Create a warm, energetic space where dog lovers instantly feel welcomed and confident they’re finding genuine savings for their furry friends. Everything from the layout to the smallest icon should reinforce trust, delight, and simplicity.
2. Visual Personality
Color Palette: Soft, cheerful hues—think warm yellows and gentle blues—that evoke sunshine and playfulness without overwhelming.
Typography:
Headings: A modern, friendly sans‑serif (like Inter) with open letterforms to feel approachable.
Body Copy: Highly legible sans‑serif with generous line spacing for comfort on small screens.
Accent Font: A slightly quirky, hand‑drawn style used sparingly for coupon codes and special call‑outs, giving a personal, “paw‑picked” touch.
Imagery & Icons: Real‑life photographs of happy dogs interspersed with clean line‑icons of bones, paw prints, and hearts. Rounded shapes and subtle shadows keep the look soft and contemporary.
3. Layout & Hierarchy
Hero Area:
Full‑bleed image of a joyful dog, overlaid with a single, punchy tagline (“Save on everything your dog loves”).
Prominent search bar centered to invite exploration.
Offer Grid:
Generous white space around each coupon card so the eye can rest and scan easily.
Coupon cards feature a bold discount label, brand logo, and a friendly “Get Deal” button.
A playful “Copied!” animation briefly replaces the button once the code is grabbed.
Navigation:
A fixed header with clear category labels (Food, Toys, Health, Services).
A secondary “Popular Stores” carousel below to spotlight key partners.
4. Interaction & Motion
Micro‑interactions:
Hover state for cards subtly lifts the card and deepens its shadow, inviting a click.
Copy‑code button pulses once on hover, hinting at its one‑click magic.
Transitions:
Smooth fades between deal filters and search results to reassure users that the site is responding.
Loading indicators shaped like spinning collars or wagging tails to keep the theme consistent.
5. Accessibility & Inclusivity
Ensure all text meets contrast standards so every pet parent—regardless of vision—can read offers with ease.
Interactive elements sized for easy tapping on touchscreens.
Alt‑text for all imagery describing dogs, products, and actions for screen‑reader users.
6. Emotional Tone
From the moment someone lands on TailMart.com, they should feel the joy of treating their dog without guilt. Friendly copy (“Your pup deserves the best for less”) paired with bright visuals will create a sense of community and shared passion.
7. Success by Design
Scan‑ability: Users should spot great deals in under two seconds.
Trust Signals: Badges (“Verified Savings”), clear expiration dates, and reviewer star icons should feel earned and prominent.
Return Visits: A “My Favorite Deals” heart icon encourages saving and returning, reinforced by subtle reminders in the UI.
This design approach keeps dog lovers front and center—making sure every graphic, font choice, and interaction feels like it was lovingly tailored for them.

Target Market(s)

Dog Lovers looking for good deals

Industry/Entity Type

Coupon Code

Number of Pages Required

4 page

Font styles to use
Sans Serif

Requirements
Must have
• Modern look, coupon copy cards it's a deal site and I want the coupon code and copy in the coupon card, blog section, review section, modern footer/header
Nice to have
• Modern coupon code website, easy to use

```html
<!DOCTYPE html>
<html lang="en">
<head>
<meta charset="utf-8">
<title>Tailmart – Dog Coupon Deals</title>
<link href="https://fonts.googleapis.com/css2?family=Poppins:wght@400;500;600;700&family=Inter:wght@400;500;600&family=Playball&display=swap" rel="stylesheet">
<style>
:root{
  --navy:#111a5c;
  --orange:#f26b35;
  --hero:#d6c3a6;
  --sky:#e0f2fb;
  --blush:#f7ede9;
  --lav:#efeef9;
  --cream:#f5ede3;
  --ink:#1b1f3b;
  --muted:#6b6f80;
  --line:#e4e4ea;
}
*{margin:0;padding:0;box-sizing:border-box}
html,body{width:1200px;height:4967px;overflow:hidden}
body{position:relative;background:#fff;font-family:Inter,sans-serif;color:var(--ink)}
.abs{position:absolute}
h2{font-family:Poppins,sans-serif;font-weight:700;color:var(--navy);font-size:38px}
.center{left:0;width:1200px;text-align:center}
.btn{display:inline-flex;align-items:center;justify-content:center;background:var(--orange);color:#fff;font-family:Poppins,sans-serif;font-weight:600;border-radius:30px;font-size:16px}
.arrow{width:24px;height:24px;border-radius:50%;display:flex;align-items:center;justify-content:center}
.arrow.grey{background:#8a8a8a}
.arrow.or{background:var(--orange)}
.photo{border-radius:0}
/* top bar */
.topbar{top:0;left:0;width:1200px;height:39px;background:var(--navy);display:flex;align-items:center;justify-content:center;gap:14px;color:#fff;font-size:13px}
.topbar .pill{background:#c9e4f6;color:var(--navy);font-weight:600;padding:3px 14px;border-radius:12px;font-size:12px}
.header{top:39px;left:0;width:1200px;height:81px}
.logo{font-family:Poppins,sans-serif;font-weight:700;color:var(--navy);font-size:28px;display:flex;align-items:center;gap:8px}
.logo .dot{width:16px;height:16px;border-radius:50%;background:var(--navy)}
.search{left:351px;top:20px;width:498px;height:42px;border:1px solid #d5d5dc;border-radius:22px;background:#f5f5f7;display:flex;align-items:center;padding-left:26px;font-size:15px;color:#555}
.search .go{position:absolute;right:-1px;top:-1px;width:56px;height:42px;background:var(--orange);border-radius:0 22px 22px 0;display:flex;align-items:center;justify-content:center}
.nav{top:120px;left:0;width:1200px;height:38px;background:var(--orange);display:flex;justify-content:center;align-items:center;gap:36px;color:#fff;font-family:Poppins,sans-serif;font-weight:600;font-size:14px}
/* hero */
.hero{top:158px;left:0;width:1200px;height:459px;background:var(--hero);border-radius:0 0 90px 90px;overflow:hidden}
.hero .script{left:112px;top:60px;font-family:Playball,cursive;font-size:72px;color:var(--navy)}
.hero .big{left:112px;font-family:Poppins,sans-serif;font-weight:700;color:var(--navy);font-size:50px;line-height:1}
.hero .tag{left:116px;top:264px;font-size:17px;color:#444}
.hero .btn{left:106px;top:315px;width:140px;height:46px}
.hero .photo{left:440px;top:0;width:760px;height:459px;background:linear-gradient(160deg,#d3bf9f 0%,#c9a97d 55%,#b4855a 100%)}
/* deals */
.dealcard{top:780px;width:480px;height:285px;border-radius:8px;overflow:hidden;background:var(--navy)}
.dealcard .txt{position:absolute;left:32px;top:80px;color:#fff}
.dealcard h3{font-family:Poppins,sans-serif;font-size:21px;font-weight:600}
.dealcard p{font-size:15px;margin-top:2px}
.code{margin-top:24px;display:inline-flex;border:2px solid #f3c24a;background:#d8301d;color:#fff;height:50px}
.code .c1{padding:4px 12px;font-family:Poppins,sans-serif;font-weight:700;font-size:19px;line-height:1.1}
.code .c1 small{display:block;font-size:10px;font-weight:500}
.code .c2{width:22px;background:#f3c24a}
.dealcard .get{position:absolute;left:32px;top:233px;color:#fff;font-weight:600;font-size:15px}
.dealcard .img{position:absolute;left:240px;top:0;width:240px;height:285px}
.badge{position:absolute;right:16px;top:14px;background:#fff;border-radius:6px;padding:6px 10px;font-size:12px;font-weight:600;color:#222}
/* steps */
.step{top:1258px;width:305px;height:131px;border:1px solid var(--line);border-radius:8px;background:#fff}
.step .ic{position:absolute;left:18px;top:34px;width:60px;height:60px;border-radius:50%;background:#f3f3f7;display:flex;align-items:center;justify-content:center}
.step h4{position:absolute;left:95px;top:30px;font-size:17px;font-weight:600;color:var(--navy)}
.step p{position:absolute;left:95px;top:56px;width:190px;font-size:12.5px;color:var(--muted);line-height:1.55}
.step .num{position:absolute;right:30px;top:-10px;width:22px;height:22px;border-radius:50%;background:#cfe9f7;color:var(--navy);font-size:12px;font-weight:600;display:flex;align-items:center;justify-content:center}
/* coupons */
.coupons-bg{top:1466px;left:0;width:1200px;height:566px;background:var(--sky);border-radius:0 0 90px 90px}
.ccard{top:1613px;width:218px;height:345px;background:#fff;border-radius:6px;overflow:hidden;box-shadow:0 2px 8px rgba(0,0,0,.06)}
.ccard .img{height:137px}
.ccard .mini{position:absolute;left:14px;top:122px;width:48px;height:30px;border-radius:5px;background:#fff;box-shadow:0 1px 4px rgba(0,0,0,.2);display:flex;align-items:center;justify-content:center}
.ccard .mini span{width:14px;height:14px;border-radius:50%;background:#3fae49}
.ccard .off{position:absolute;left:15px;top:176px;font-size:14px;font-weight:600}
.ccard .use{position:absolute;left:15px;top:204px;background:#dceefa;color:var(--navy);font-size:13px;padding:5px 12px;border-radius:5px}
.ccard h4{position:absolute;left:15px;top:245px;font-family:Poppins,sans-serif;font-size:20px;font-weight:600;color:var(--navy)}
.ccard .btn{position:absolute;left:14px;top:286px;width:124px;height:40px;font-size:15px}
/* trending */
.side{top:2201px;left:104px;width:224px;height:400px;border:1px solid var(--line);background:#fff}
.side .item{position:absolute;left:0;width:224px;height:74px;display:flex;align-items:center;gap:16px;padding-left:18px;font-size:16px;font-weight:600;color:var(--navy);line-height:1.3}
.side .item .c{width:48px;height:48px;border-radius:50%;background:#f3f3f7;border:1px solid #e4e4ea}
.side .item.on{background:#f8ece6;color:var(--orange)}
.offers{top:2201px;left:353px;width:737px;height:75px;border:1px solid var(--line);background:#fcf8f6;display:flex;align-items:center;justify-content:space-between;padding:0 24px;font-weight:600;font-size:16px}
.offers .more{color:var(--orange);font-size:15px}
.tcard{top:2331px;width:220px;height:268px;border:1px solid var(--line);border-radius:6px;background:#fff}
.tcard .brand{position:absolute;left:22px;top:28px;font-family:Poppins,sans-serif;font-weight:600;font-size:13px;color:var(--navy);display:flex;align-items:center;gap:5px}
.tcard .brand i{width:10px;height:10px;background:var(--orange);border-radius:50%}
.tcard h4{position:absolute;left:22px;top:88px;width:180px;font-family:Poppins,sans-serif;font-size:19px;font-weight:600;color:var(--navy);line-height:1.25}
.tcard .pct{position:absolute;left:22px;top:152px;color:var(--orange);font-size:15px;font-weight:600}
.tcard .btn{position:absolute;left:22px;top:192px;width:176px;height:42px}
/* stores */
.stores-bg{top:2697px;left:0;width:1200px;height:693px;background:var(--blush);border-radius:90px 90px 0 0}
.scard{background:#fff;border:1px solid #eadfd9;border-radius:4px}
.scard .name{position:absolute;left:0;right:0;text-align:center;font-family:Poppins,sans-serif;font-weight:700;color:var(--navy)}
.scard .pct{position:absolute;left:0;right:0;text-align:center;color:var(--orange);font-weight:600;font-size:17px}
/* testimonials */
.tbox{top:3583px;width:322px;height:214px;background:var(--lav);border-radius:4px;padding:30px 28px;font-size:12px;line-height:1.75;color:#333}
.stars{color:var(--orange);font-size:14px;letter-spacing:3px;margin-bottom:8px}
.tbox .who{margin-top:10px;font-size:11px;color:#555}
/* newsletter */
.news{top:4051px;left:106px;width:986px;height:344px;background:var(--orange);border-radius:4px}
.woman{left:116px;top:3878px;width:464px;height:517px;background:linear-gradient(180deg,#e8d9c8 0%,#b9875e 60%,#8c5f3c 100%);border-radius:230px 230px 0 0}
.news h3{position:absolute;left:479px;top:48px;font-family:Poppins,sans-serif;font-weight:700;color:#fff;font-size:40px;line-height:1.2}
.news p{position:absolute;left:479px;top:152px;color:#fde3d6;font-size:14px;line-height:1.5;width:320px}
.news .field{position:absolute;left:479px;top:218px;width:444px;height:53px;background:#fff;border-radius:28px;font-size:13px;color:#666;padding:18px 22px}
.news .field .sub{position:absolute;right:4px;top:4px;height:45px;width:184px;border-radius:24px;background:var(--navy);color:#fff;font-weight:600;font-size:16px;display:flex;align-items:center;justify-content:center}
.feat{top:4455px;display:flex;gap:12px;align-items:center}
.feat .ic{width:26px;height:26px}
.feat b{display:block;font-size:13px;font-weight:600;color:var(--navy)}
.feat span{font-size:10px;color:#555}
/* footer */
.footer{top:4557px;left:0;width:1200px;height:410px;background:var(--cream);border-radius:90px 90px 0 0}
.fcol{top:4665px}
.fcol h5{font-size:17px;font-weight:600;color:var(--navy);margin-bottom:24px;position:relative}
.fcol h5:after{content:"";position:absolute;left:0;bottom:-8px;width:44px;height:2px;background:var(--orange)}
.fcol a{display:block;font-size:13px;color:#555;margin-bottom:22px;text-decoration:none}
.vline{top:4625px;width:1px;height:250px;background:#d9cfc3}
.soc{width:30px;height:30px;border-radius:50%;border:1px solid #999;background:#fff}
.copy{top:4922px;left:0;width:1200px;text-align:center;font-size:13px;color:#444}
</style>
</head>
<body>

<div class="abs topbar"><span class="pill">10% Off</span><span>Welcome to Tailmart - &nbsp;Trusted Coupons, Offers</span></div>

<header class="abs header">
  <div class="abs logo" style="left:67px;top:22px"><span class="dot"></span>Tailmart</div>
  <div class="abs search">Search
    <span class="go"><svg width="20" height="20" viewBox="0 0 20 20" fill="none" stroke="#fff" stroke-width="2.4"><circle cx="9" cy="9" r="6"/><path d="M13.5 13.5 18 18"/></svg></span>
  </div>
  <svg class="abs" style="left:943px;top:29px" width="26" height="26" viewBox="0 0 24 24" fill="none" stroke="#111" stroke-width="1.6"><path d="M6 4h12l4 5-10 12L2 9z"/><path d="M2 9h20M9 4l3 17 3-17"/></svg>
  <svg class="abs" style="left:1004px;top:31px" width="26" height="24" viewBox="0 0 24 22" fill="none" stroke="#111" stroke-width="1.8"><path d="M12 20S2 13.5 2 7a5 5 0 0 1 10-1 5 5 0 0 1 10 1c0 6.5-10 13-10 13z"/></svg>
  <svg class="abs" style="left:1063px;top:29px" width="26" height="28" viewBox="0 0 24 26" fill="none" stroke="#111" stroke-width="1.8"><circle cx="12" cy="8" r="5"/><path d="M3 25c0-6 4-9 9-9s9 3 9 9"/></svg>
</header>

<nav class="abs nav"><span>CATEGORIES ⌄</span><span>POPULAR STORES</span><span>LATEST DEALS</span></nav>

<section class="abs hero">
  <div class="abs photo" role="img" aria-label="Happy labrador beside a pile of dog toys, plush teddy, brushes and a food bowl"></div>
  <div class="abs script">Save On</div>
  <div class="abs big" style="top:138px">Everything</div>
  <div class="abs big" style="top:196px">Your Dog Loves</div>
  <div class="abs tag">Your pup deserves the best for less</div>
  <div class="abs btn">Get Deal →</div>
</section>

<h2 class="abs center" style="top:682px">Popular Deal</h2>
<div class="abs arrow grey" style="left:60px;top:902px"><svg width="10" height="10" viewBox="0 0 10 10"><path d="M7 1 3 5l4 4" stroke="#fff" stroke-width="2" fill="none"/></svg></div>
<div class="abs arrow or" style="left:1116px;top:902px"><svg width="10" height="10" viewBox="0 0 10 10"><path d="M3 1l4 4-4 4" stroke="#fff" stroke-width="2" fill="none"/></svg></div>

<div class="abs dealcard" style="left:108px">
  <div class="txt"><h3>Upto 50-80% Off</h3><p>On Latest Food</p>
    <div class="code"><div class="c1">CD499<small>USE CODE</small></div><div class="c2"></div></div></div>
  <div class="get">Get Deal →</div>
  <div class="img" role="img" aria-label="Bag of premium lamb and rice dog food with a bowl of kibble" style="background:linear-gradient(180deg,#f3f0ec,#e2d8cc)"></div>
  <div class="badge">shopzone</div>
</div>
<div class="abs dealcard" style="left:612px">
  <div class="txt"><h3>Upto 50-80% Off</h3><p>On Latest Food</p>
    <div class="code"><div class="c1">CD499<small>USE CODE</small></div><div class="c2"></div></div></div>
  <div class="get">Get Deal →</div>
  <div class="img" role="img" aria-label="Pink pouch of cat food on a blue background" style="background:linear-gradient(180deg,#3a8dc7,#2a6fa8)"></div>
  <div class="badge">shopzone</div>
</div>

<h2 class="abs" style="left:108px;top:1160px">Three Steps To Save With Tailmart</h2>
<div class="abs step" style="left:108px"><span class="num">1</span><div class="ic"><svg width="30" height="30" viewBox="0 0 24 24" fill="none" stroke="#3b4a8c" stroke-width="1.5"><circle cx="10" cy="8" r="4"/><path d="M3 21c0-5 3-8 7-8s7 3 7 8"/></svg></div><h4>Log In</h4><p>Lorem Ipsum has been the industry's standard</p></div>
<div class="abs step" style="left:447px"><span class="num">2</span><div class="ic"><svg width="32" height="24" viewBox="0 0 32 24" fill="none" stroke="#3b4a8c" stroke-width="1.5"><rect x="2" y="4" width="28" height="16" rx="2"/><path d="M12 16l8-8"/><circle cx="12" cy="9" r="1.5"/><circle cx="20" cy="15" r="1.5"/></svg></div><h4>Use Code</h4><p>Lorem Ipsum has been the industry's standard</p></div>
<div class="abs step" style="left:787px"><span class="num">3</span><div class="ic"><svg width="30" height="30" viewBox="0 0 24 24" fill="none" stroke="#3b4a8c" stroke-width="1.5"><path d="M2 18h5l6 2 9-5-2-2-6 3h-4"/><circle cx="14" cy="7" r="4" stroke="#f26b35"/></svg></div><h4>Get Reward</h4><p>Lorem Ipsum has been the industry's standard</p></div>

<div class="abs coupons-bg"></div>
<h2 class="abs center" style="top:1525px">Coupon Cards</h2>
<div class="abs arrow grey" style="left:60px;top:1776px"><svg width="10" height="10" viewBox="0 0 10 10"><path d="M7 1 3 5l4 4" stroke="#fff" stroke-width="2" fill="none"/></svg></div>
<div class="abs arrow or" style="left:1116px;top:1776px"><svg width="10" height="10" viewBox="0 0 10 10"><path d="M3 1l4 4-4 4" stroke="#fff" stroke-width="2" fill="none"/></svg></div>

<div class="abs ccard" style="left:108px"><div class="img" role="img" aria-label="Bulldog playing with a rope toy" style="background:linear-gradient(160deg,#b77a54,#e2c0a0)"></div><div class="mini"><span></span></div><div class="off">Upto 50-80% Off</div><div class="use">🏷 Use Code</div><h4>Lorem Ipsum</h4><div class="btn">Get Deal →</div></div>
<div class="abs ccard" style="left:363px"><div class="img" role="img" aria-label="Terrier chasing a ball on a yellow background" style="background:linear-gradient(160deg,#f2b23a,#e89a23)"></div><div class="mini"><span></span></div><div class="off">Upto 50-80% Off</div><div class="use">🏷 Use Code</div><h4>Lorem Ipsum</h4><div class="btn">Get Deal →</div></div>
<div class="abs ccard" style="left:617px"><div class="img" role="img" aria-label="Fluffy dog next to grooming scissors on a blue background" style="background:linear-gradient(160deg,#4d8fd1,#2f6fb8)"></div><div class="mini"><span></span></div><div class="off">Upto 50-80% Off</div><div class="use">🏷 Use Code</div><h4>Lorem Ipsum</h4><div class="btn">Get Deal →</div></div>
<div class="abs ccard" style="left:872px"><div class="img" role="img" aria-label="Treat pouch surrounded by dog biscuits" style="background:linear-gradient(160deg,#3f73b8,#c9a25a)"></div><div class="mini"><span></span></div><div class="off">Upto 50-80% Off</div><div class="use">🏷 Use Code</div><h4>Lorem Ipsum</h4><div class="btn">Get Deal →</div></div>

<h2 class="abs" style="left:103px;top:2096px">Trending Categories</h2>
<div class="abs side">
  <div class="item on" style="top:0"><span class="c"></span>Dog Food &amp;<br>Treats</div>
  <div class="item" style="top:100px"><span class="c"></span>Toys &amp;<br>Accessories</div>
  <div class="item" style="top:206px"><span class="c"></span>Health &amp;<br>Grooming</div>
  <div class="item" style="top:312px"><span class="c"></span>Training &amp;<br>Services</div>
</div>
<svg class="abs" style="left:328px;top:2228px" width="10" height="18"><path d="M0 0l10 9-10 9z" fill="#f26b35"/></svg>
<div class="abs offers"><span>Offers</span><span class="more">Show More →</span></div>
<div class="abs tcard" style="left:353px"><div class="brand"><i></i>Stagehall</div><h4>Lorem Ipsum is simply dummy</h4><div class="pct">🏷 Upto 50-80% Off</div><div class="btn">Get Deal →</div></div>
<div class="abs tcard" style="left:612px"><div class="brand"><i></i>Stagehall</div><h4>Lorem Ipsum is simply dummy</h4><div class="pct">🏷 Upto 50-80% Off</div><div class="btn">Get Deal →</div></div>
<div class="abs tcard" style="left:870px"><div class="brand"><i></i>Stagehall</div><h4>Lorem Ipsum is simply dummy</h4><div class="pct">🏷 Upto 50-80% Off</div><div class="btn">Get Deal →</div></div>

<div class="abs stores-bg"></div>
<h2 class="abs center" style="top:2764px">Top Stores</h2>
<div class="abs scard" style="left:108px;top:2871px;width:344px;height:376px">
  <div class="abs" style="left:12px;top:12px;width:318px;height:200px;border:1px solid #e5e5e5;border-radius:3px"></div>
  <div class="name" style="top:90px;font-size:28px">Trilane</div>
  <div class="abs" style="right:28px;top:26px;width:26px;height:26px;border-radius:50%;background:var(--orange)"></div>
  <div class="name" style="top:252px;font-size:22px;font-weight:600">Lorem Ipsum</div>
  <div class="pct" style="top:300px">🏷 Upto 50-80% Off</div>
</div>
<div class="abs scard" style="left:477px;top:2871px;width:185px;height:173px"><div class="name" style="top:46px;font-size:16px">Daltrix</div><div class="pct" style="top:128px">🏷 Upto 6-7%</div></div>
<div class="abs scard" style="left:691px;top:2871px;width:185px;height:173px"><div class="name" style="top:46px;font-size:16px">Dovera</div><div class="pct" style="top:128px">🏷 Upto 6-7%</div></div>
<div class="abs scard" style="left:905px;top:2871px;width:185px;height:173px"><div class="name" style="top:46px;font-size:16px">Daltrix</div><div class="pct" style="top:128px">🏷 Upto 6-7%</div></div>
<div class="abs scard" style="left:477px;top:3081px;width:185px;height:170px"><div class="name" style="top:46px;font-size:16px">Arcona</div><div class="pct" style="top:128px">🏷 Upto 6-7%</div></div>
<div class="abs scard" style="left:691px;top:3081px;width:185px;height:170px"><div class="name" style="top:46px;font-size:16px">Daltrix</div><div class="pct" style="top:128px">🏷 Upto 6-7%</div></div>
<div class="abs scard" style="left:905px;top:3081px;width:185px;height:170px"><div class="name" style="top:46px;font-size:16px">Leafcorp</div><div class="pct" style="top:128px">🏷 Upto 6-7%</div></div>
<div class="abs arrow grey" style="left:559px;top:3291px"><svg width="10" height="10" viewBox="0 0 10 10"><path d="M7 1 3 5l4 4" stroke="#fff" stroke-width="2" fill="none"/></svg></div>
<div class="abs arrow or" style="left:616px;top:3291px"><svg width="10" height="10" viewBox="0 0 10 10"><path d="M3 1l4 4-4 4" stroke="#fff" stroke-width="2" fill="none"/></svg></div>

<h2 class="abs center" style="top:3487px">Client Testimonial</h2>
<div class="abs tbox" style="left:102px"><div class="stars">★★★★★</div>My favourite app that gave me extra discounts and cashback on brands like Shopzone, Cartly &amp; Stylora. Using this app for a long time and I am really enjoying its features.<div class="who">Riya Desai, Navi Mumbai</div></div>
<div class="abs tbox" style="left:442px"><div class="stars">★★★★★</div>Thank You, DealNest, for providing a cashback of ₹1549 on the Vexa laptop order. I must say you are truly a genuine cashback website. This review is from the heart. You rock!<div class="who">Arun Mehta, Rudrapur</div></div>
<div class="abs tbox" style="left:781px;padding-top:22px"><div class="stars">★★★★★</div>Lot of options variety easy to choose thank you! last week I redeemed my DealNest balance to Shopzone. They gave full instructions about to redeem the amount. I redeemed my amount and feel very happy.<div class="who">Kiran Rao, Patna</div></div>
<div class="abs arrow grey" style="left:559px;top:3843px"><svg width="10" height="10" viewBox="0 0 10 10"><path d="M7 1 3 5l4 4" stroke="#fff" stroke-width="2" fill="none"/></svg></div>
<div class="abs arrow or" style="left:616px;top:3843px"><svg width="10" height="10" viewBox="0 0 10 10"><path d="M3 1l4 4-4 4" stroke="#fff" stroke-width="2" fill="none"/></svg></div>

<section class="abs news">
  <h3>Subscribe Our<br>Newsletter</h3>
  <p>It has survived not only five centuries, but also the leap into electronic</p>
  <div class="field">Enter Mail ID<span class="sub">Subscribe →</span></div>
</section>
<div class="abs woman" role="img" aria-label="Smiling woman in a brown jacket holding a small terrier puppy"></div>

<div class="abs feat" style="left:174px"><svg class="ic" viewBox="0 0 24 24" fill="none" stroke="#f26b35" stroke-width="1.5"><path d="M3 7h11v9H3zM14 10h4l3 3v3h-7"/><circle cx="7" cy="18" r="2"/><circle cx="17" cy="18" r="2"/></svg><div><b>Free Shipping</b><span>On all orders above ₹499</span></div></div>
<div class="abs feat" style="left:411px"><svg class="ic" viewBox="0 0 24 24" fill="none" stroke="#f26b35" stroke-width="1.5"><path d="M20 12a8 8 0 1 1-3-6.2M20 4v5h-5"/></svg><div><b>Free Returns</b><span>Within 7 days(T&amp;Cs Apply)</span></div></div>
<div class="abs feat" style="left:646px"><svg class="ic" viewBox="0 0 24 24" fill="none" stroke="#f26b35" stroke-width="1.5"><circle cx="12" cy="12" r="9"/><path d="M12 7v6M12 16v1"/></svg><div><b>Best Deals</b><span>On Pet Products</span></div></div>
<div class="abs feat" style="left:882px"><svg class="ic" viewBox="0 0 24 24" fill="none" stroke="#f26b35" stroke-width="1.5"><circle cx="12" cy="12" r="9"/><circle cx="12" cy="12" r="4"/></svg><div><b>We Support</b><span>Monday-Saturday,9am to<br>9pm</span></div></div>

<footer class="abs footer"></footer>
<div class="abs logo" style="left:106px;top:4660px"><span class="dot"></span>Tailmart</div>
<p class="abs" style="left:106px;top:4720px;width:260px;font-size:13px;color:#555;line-height:1.6">Lorem Ipsum has been the industry's standard</p>
<div class="abs" style="left:106px;top:4800px;display:flex;gap:10px"><span class="soc"></span><span class="soc"></span><span class="soc"></span><span class="soc"></span><span class="soc"></span></div>
<div class="abs vline" style="left:376px"></div>
<div class="abs vline" style="left:627px"></div>
<div class="abs vline" style="left:878px"></div>
<div class="abs fcol" style="left:440px"><h5>Information</h5><a>List Your Business</a><a>Privacy Policy</a><a>Terms &amp; Conditions</a></div>
<div class="abs fcol" style="left:698px"><h5>Categories</h5><a>Hot Deal</a><a>Popular stores</a><a>Latest deals</a></div>
<div class="abs fcol" style="left:955px"><h5>How It Works</h5><a>FAQs</a><a>How It Works</a><a>Contact Us</a></div>
<div class="abs copy">© 2025, <b>TAILMART.</b> All Rights Reserved.</div>

</body>
</html>
```